Boutique raw honey label from Australia. Blue mountains clean environment

I need a quirky Eco label for a raw honey product to appeal to boutique honey buyers with Gm free 100% raw honey included. Honey come from blue mountains a world heritage listed area in nsw Aust.
Want to appeal to people who love good food and love beautiful things and who want to know where there food comes from and how it is grown. Gm free, pesticide free, hand poured family run and owned business

Target Market(s)

Health conscious, lovers of fine food

Industry/Entity Type

Environment

Font styles to use
Other font styles liked:
• Courier

Requirements
Must have
• 100% Raw
Nice to have
• A little blurb about where honey is from
• # please see my current label - something similar to this but with a vintage bee design possibly

```html
<!DOCTYPE html>
<html lang="en">
<head>
<meta charset="utf-8">
<title>Melvane Gourmet Honey – Label Set</title>
<link rel="stylesheet" href="https://fonts.googleapis.com/css2?family=Cinzel:wght@600&family=Courier+Prime:wght@400;700&family=Open+Sans:wght@400&display=swap">
<style>
  :root {
    --canvas: #ffffff;
    --gold: #a3873c;
    --gold-soft: #b89b52;
    --cream-top: #efece5;
    --cream-bottom: #e2ded4;
    --ink-dark: #353432;
    --black-top: #1b1b1b;
    --black-bottom: #0b0b0b;
    --ink-muted: #85836f;
    --ink-volume-dark: #b7b3a4;
    --amber-honey: #8b2f0b;
    --set-honey: #d8bf88;
  }
  * { box-sizing: border-box; margin: 0; padding: 0; }
  html, body { width: 1200px; height: 1000px; overflow: hidden; background: var(--canvas); }
  .canvas { position: relative; width: 1200px; height: 1000px; }

  .label {
    position: absolute;
    top: 310px;
    width: 438px;
    height: 380px;
    text-align: center;
  }
  .label--amber { left: 128px; background: linear-gradient(180deg, var(--cream-top), var(--cream-bottom)); color: var(--ink-dark); --honey: var(--amber-honey); --volume: var(--ink-dark); }
  .label--set { left: 642px; background: linear-gradient(180deg, var(--black-top), var(--black-bottom)); color: var(--ink-muted); --honey: var(--set-honey); --volume: var(--ink-volume-dark); }

  .label__frame {
    position: absolute;
    inset: 12px 10px 12px 10px;
    border: 1.5px solid var(--gold);
  }
  .label__drip { position: absolute; left: 50%; top: 0; width: 70px; height: 64px; transform: translateX(-50%); }

  .label__corner {
    position: absolute;
    width: 78px;
    height: 66px;
    background: radial-gradient(circle at 30% 30%, rgba(163,135,60,0.55), rgba(163,135,60,0.12) 70%);
    border-radius: 4px;
  }
  .label__corner--tl { top: 18px; left: 16px; }
  .label__corner--tr { top: 18px; right: 16px; }
  .label__corner--bl { bottom: 18px; left: 16px; }
  .label__corner--br { bottom: 18px; right: 16px; }

  .label__brand {
    position: absolute; left: 0; right: 0; top: 110px;
    font-family: "Cinzel", serif; font-weight: 600;
    font-size: 42px; line-height: 1; letter-spacing: 0.5px;
    color: var(--gold);
  }
  .label__type {
    position: absolute; left: 0; right: 0; top: 182px;
    font-family: "Courier Prime", "Courier New", monospace;
    font-size: 17px; letter-spacing: 4.5px; line-height: 1;
  }
  .label__claim {
    position: absolute; left: 0; right: 0; top: 207px;
    font-family: "Courier Prime", "Courier New", monospace; font-weight: 700;
    font-size: 21px; letter-spacing: 2px; line-height: 1;
  }
  .label__bee {
    position: absolute; left: 50%; top: 247px; width: 46px; height: 40px;
    transform: translateX(-50%);
    background: radial-gradient(ellipse at center, var(--gold-soft), rgba(163,135,60,0.25) 70%);
    border-radius: 50%;
  }
  .label__blurb {
    position: absolute; left: 0; right: 0; top: 305px;
    font-family: "Courier Prime", "Courier New", monospace; font-weight: 700;
    font-size: 15.5px; line-height: 21px;
  }
  .label__rule { position: absolute; left: 50%; top: 357px; width: 92px; transform: translateX(-50%); height: 0; border-top: 1.5px solid var(--gold); }
  .label__rule--lower { top: 361px; width: 60px; border-top-width: 1px; }
  .label__volume {
    position: absolute; left: 0; right: 0; top: 372px;
    font-family: "Open Sans", sans-serif; font-size: 15px; line-height: 1;
    color: var(--volume);
  }
  /* vertical offsets relative to label start */
  .label__content { position: absolute; inset: 0; top: -40px; }
</style>
</head>
<body>
<main class="canvas">

  <section class="label label--amber" aria-label="Melvane raw honey label, cream edition">
    <div class="label__frame"></div>
    <div class="label__corner label__corner--tl" role="img" aria-label="Gold filigree corner ornament"></div>
    <div class="label__corner label__corner--tr" role="img" aria-label="Gold filigree corner ornament"></div>
    <div class="label__corner label__corner--bl" role="img" aria-label="Gold filigree corner ornament"></div>
    <div class="label__corner label__corner--br" role="img" aria-label="Gold filigree corner ornament"></div>
    <svg class="label__drip" viewBox="0 0 70 64" aria-hidden="true">
      <path d="M0 0 H70 C50 0 42 6 40 22 C39 30 46 36 46 46 C46 53 41 58 35 58 C29 58 24 53 24 46 C24 36 31 30 30 22 C28 6 20 0 0 0 Z" fill="var(--honey)"/>
    </svg>
    <div class="label__content">
      <h1 class="label__brand">Melvane</h1>
      <p class="label__type">GOURMET HONEY</p>
      <p class="label__claim">100% RAW</p>
      <div class="label__bee" role="img" aria-label="Vintage engraved bee illustration in gold"></div>
      <p class="label__blurb">Wild honey. Natural beekeeping<br>originating of Blue Mountains.</p>
      <div class="label__rule"></div>
      <div class="label__rule label__rule--lower"></div>
      <p class="label__volume">℮ 100ml | 3.3 FL.OZ.</p>
    </div>
  </section>

  <section class="label label--set" aria-label="Melvane raw honey label, black edition">
    <div class="label__frame"></div>
    <div class="label__corner label__corner--tl" role="img" aria-label="Gold filigree corner ornament"></div>
    <div class="label__corner label__corner--tr" role="img" aria-label="Gold filigree corner ornament"></div>
    <div class="label__corner label__corner--bl" role="img" aria-label="Gold filigree corner ornament"></div>
    <div class="label__corner label__corner--br" role="img" aria-label="Gold filigree corner ornament"></div>
    <svg class="label__drip" viewBox="0 0 70 64" aria-hidden="true">
      <path d="M0 0 H70 C50 0 42 6 40 22 C39 30 46 36 46 46 C46 53 41 58 35 58 C29 58 24 53 24 46 C24 36 31 30 30 22 C28 6 20 0 0 0 Z" fill="var(--honey)"/>
    </svg>
    <div class="label__content">
      <h1 class="label__brand">Melvane</h1>
      <p class="label__type">GOURMET HONEY</p>
      <p class="label__claim">100% RAW</p>
      <div class="label__bee" role="img" aria-label="Vintage engraved bee illustration in gold"></div>
      <p class="label__blurb">Wild honey. Natural beekeeping<br>originating of Blue Mountains.</p>
      <div class="label__rule"></div>
      <div class="label__rule label__rule--lower"></div>
      <p class="label__volume">℮ 100ml | 3.3 FL.OZ.</p>
    </div>
  </section>

</main>
</body>
</html>
```